VFX Company Business Card Design Project

The Ember Vale is a decentralized Visual Effects Studio servicing the television and feature film industries.
Project Brief:
Take our logo that was previously designed on Pixel Harbor and make a double sided business card.
Requirements:
- Card MUST be double sided.
- Front of card MUST have the yellow part of our logo against the dark grey background.
- Back of card is completely up to the designer.
- Back of card must include the complete company logo.
Please follow these File Preparation guidelines:
http://printmoor.example/infopage?file=filetype_en&s=PrintMoor_new&lang=en
Industry/Entity Type
Business
Look and feel
Each slider illustrates characteristics of the customer's brand and the style your logo design should communicate.

```html
<!DOCTYPE html>
<html lang="en">
<head>
<meta charset="utf-8">
<title>The Ember Vale – Business Card</title>
<link href="https://fonts.googleapis.com/css2?family=Arimo:wght@400;700&display=swap" rel="stylesheet">
<style>
  :root {
    --page: #ffffff;
    --panel: #f0f0f0;
    --panel-edge: #333333;
    --card-dark: #1d1d1d;
    --brand-yellow: #fbc41a;
    --slate: #3d5868;
    --logo-light: #cfd6da;
  }
  * { box-sizing: border-box; margin: 0; padding: 0; }
  html, body {
    width: 879px; height: 1200px; overflow: hidden;
    background: var(--page);
    font-family: "Arimo", Arial, sans-serif;
  }
  .sheet { position: relative; width: 879px; height: 1200px; }
  .card-panel {
    position: absolute; left: 14px; width: 854px;
    background: var(--panel);
    border: 4px dotted var(--panel-edge);
  }
  .card-panel--front { top: 14px; height: 510px; }
  .card-panel--back { top: 687px; height: 500px; }
  .card {
    position: absolute; left: 40px; top: 32px; width: 776px; height: 441px;
    background: var(--brand-yellow); overflow: hidden;
  }
  .card-panel--back .card { background: var(--card-dark); }
  .card__shape { position: absolute; inset: 0; width: 100%; height: 100%; }
  .card__title {
    position: absolute; right: 24px; top: 52px;
    font-size: 40px; font-weight: 700; color: var(--slate);
  }
  .contact {
    position: absolute; right: 24px; top: 205px;
    text-align: right; color: var(--slate);
    font-style: normal; font-size: 30px; line-height: 46px;
  }
  .contact__name { font-weight: 700; }
  .brand {
    position: absolute; display: flex; align-items: center; gap: 14px;
    font-size: 36px; font-weight: 700; color: var(--logo-light);
    white-space: nowrap;
  }
  .brand__dot {
    width: 30px; height: 30px; border-radius: 50%;
    background: var(--brand-yellow); flex: none;
  }
  .brand--front { left: 40px; top: 250px; }
  .brand--back { right: 36px; top: 72px; }
</style>
</head>
<body>
<main class="sheet">
  <section class="card-panel card-panel--front" aria-label="Card front">
    <div class="card">
      <svg class="card__shape" viewBox="0 0 776 441" preserveAspectRatio="none" aria-hidden="true">
        <path d="M0 0 H230 C370 50 450 200 465 441 H0 Z" fill="var(--card-dark)"/>
      </svg>
      <div class="brand brand--front"><span class="brand__dot"></span>The Ember Vale</div>
      <h1 class="card__title">Ember Vale</h1>
      <address class="contact">
        <div class="contact__name">Marlow Denn</div>
        <div class="contact__role">Owner</div>
        <div class="contact__email">hello@embervale</div>
        <div class="contact__phone">555.210.4836</div>
      </address>
    </div>
  </section>

  <section class="card-panel card-panel--back" aria-label="Card back">
    <div class="card">
      <svg class="card__shape" viewBox="0 0 776 441" aria-hidden="true">
        <circle cx="150" cy="430" r="190" fill="var(--brand-yellow)"/>
      </svg>
      <div class="brand brand--back"><span class="brand__dot"></span>The Ember Vale</div>
    </div>
  </section>
</main>
</body>
</html>
```